Letterhead and Envelope Only (no biz card)
Leadership Development & Coaching Start Up
I also really like it when the swirls are not perfectly positioned on the page...bleeding off the page looks good. Thanks everyone!
Thanks for submitting your designs! Something else to keep in mind, I am rather feminine...I prefer softer lines and fainter watermarks in the background. I also really prefer the contact info to be on the bottom of the design.
Correction, I like the contact info on the bottom in #1 (not #3.)
My logo designer is out of the country, I should have those files for you in the next couple of days.
From the three designs so far, I like the swirls in #2. I like the contact info on the bottom in #3.
If possible, I'd like to have 2 letterhead designs in my winner...so I can use both for various purposes.
could you please upload the ai or eps file of logo?

```html
<!DOCTYPE html>
<html lang="en">
<head>
<meta charset="utf-8">
<title>Velmora Stationery</title>
<link href="https://fonts.googleapis.com/css2?family=Questrial&family=Open+Sans:wght@400&display=swap" rel="stylesheet">
<style>
  :root {
    --navy: #1f3b7a;
    --gold: #f2b519;
    --orange: #f08a1c;
    --paper: #ffffff;
    --swirl: #fbe6c4;
    --backdrop: #e9e6df;
    --ink: #3a3a3a;
  }
  html, body { margin: 0; padding: 0; overflow: hidden; }
  body { width: 1200px; height: 1057px; background: var(--backdrop); position: relative; }

  .letterhead {
    position: absolute; left: 614px; top: 57px; width: 515px; height: 949px;
    background: var(--paper); box-shadow: 0 4px 14px rgba(0,0,0,.18); overflow: hidden;
  }
  .letterhead .watermark {
    position: absolute; left: 60px; top: 150px; width: 520px; height: 720px;
    background: radial-gradient(ellipse at 55% 45%, var(--swirl) 0%, rgba(251,230,196,.35) 45%, rgba(255,255,255,0) 72%);
  }
  .brand {
    position: absolute; display: flex; align-items: center; gap: 6px;
    font-family: "Questrial", sans-serif; color: var(--navy); letter-spacing: .5px;
  }
  .brand .dot { border-radius: 50%; background: var(--orange); }
  .letterhead .brand { left: 50%; transform: translateX(-50%); top: 92px; font-size: 40px; }
  .letterhead .brand .dot { width: 14px; height: 14px; margin-top: -22px; }

  .contact {
    position: absolute; margin: 0; font-family: "Open Sans", sans-serif; color: var(--ink);
    white-space: nowrap; font-size: 7px; line-height: 10px;
  }
  .contact span { margin: 0 4px; color: var(--navy); }
  .letterhead .contact { left: 0; right: 0; text-align: center; top: 908px; }
  .footer-rule { position: absolute; left: 0; right: 0; }
  .letterhead .gold-rule { top: 930px; height: 2px; background: var(--gold); }
  .letterhead .navy-band { top: 933px; height: 16px; background: var(--navy); }

  .envelope {
    position: absolute; left: 34px; top: 451px; width: 800px; height: 358px;
  }
  .envelope .flap { position: absolute; left: 0; top: 0; }
  .envelope .body {
    position: absolute; left: 0; top: 91px; width: 800px; height: 267px;
    background: var(--paper); box-shadow: 0 4px 14px rgba(0,0,0,.18); overflow: hidden;
  }
  .envelope .watermark {
    position: absolute; left: 380px; top: -60px; width: 460px; height: 340px;
    background: radial-gradient(ellipse at 50% 50%, var(--swirl) 0%, rgba(251,230,196,.3) 50%, rgba(255,255,255,0) 75%);
  }
  .envelope .top-rule { position: absolute; left: 0; right: 0; top: 0; height: 4px; background: var(--gold); }
  .envelope .brand { left: 40px; top: 52px; font-size: 40px; }
  .envelope .brand .dot { width: 14px; height: 14px; margin-top: -22px; }
  .address-window {
    position: absolute; left: 94px; top: 92px; width: 380px; height: 103px;
    background: linear-gradient(#f1f1f1, #e4e4e4); border: 1px solid #d0d0d0; border-radius: 3px;
  }
  .envelope .contact { right: 24px; top: 232px; font-size: 7.5px; }
  .envelope .gold-rule { top: 250px; height: 2px; background: var(--gold); }
  .envelope .navy-band { top: 253px; height: 14px; background: var(--navy); }
</style>
</head>
<body>
  <section class="letterhead">
    <div class="watermark" role="img" aria-label="Faint soft swirl watermark pattern"></div>
    <div class="brand">velmora<span class="dot"></span></div>
    <p class="contact">4520 Alder Crest Lane, Marlow, CO 80211<span>|</span>P<span>|</span>303.555.0147<span>|</span>E<span>|</span>hello@velmoragroup.com<span>|</span>W<span>|</span>www.velmoragroup.com</p>
    <div class="footer-rule gold-rule"></div>
    <div class="footer-rule navy-band"></div>
  </section>

  <section class="envelope">
    <svg class="flap" width="800" height="95" viewBox="0 0 800 95">
      <polygon points="0,95 30,0 770,0 800,95" fill="var(--navy)"/>
    </svg>
    <div class="body">
      <div class="watermark" role="img" aria-label="Faint soft swirl watermark pattern"></div>
      <div class="top-rule"></div>
      <div class="brand">velmora<span class="dot"></span></div>
      <div class="address-window"></div>
      <p class="contact">4520 Alder Crest Lane, Marlow, CO 80211<span>|</span>P<span>|</span>303.555.0147<span>|</span>E<span>|</span>hello@velmoragroup.com<span>|</span>W<span>|</span>www.velmoragroup.com</p>
      <div class="footer-rule gold-rule"></div>
      <div class="footer-rule navy-band"></div>
    </div>
  </section>
</body>
</html>
```